Innovative and exciting banner advert for real estate
Lots of freedom of design
#10 I like the way the 'save thousands in commission' is done with mixed size font. The 'save thousands' stands out very clearly which is important to us
Thanks.
Hi and thank you designers for your attention to our project, there are some great ideas coming in now.
A slight change to the brief:
In the blue screen, please remove 'money back guarantee' and replace with 'no hidden charges' from the green screen so each screen has only 3 bullet points.
Thanks
RPellow
Hi Designers
Please note, we do not require the logo in the adverts just the use of the logo colours as the base.
It is more important that the first line of text stands out. If you are going to insert the logo, please make it a minor element or as #4 has cleverly used it for the bullet points.
Thanks designers for your time and great ideas. #4 I like the way you have used the logo symbol in the bullet points, and that you have aligned the bullets points to the left, it looks good.
#5 the way that 'save thousands' and 'get the best price' stand out clearly is great, this is the message that we are trying to pass on to viewers, it is most important.
If there is any information you need please contact me directly, I will check messages.
Just to clarify, we do not require the logo in the adverts just the use of the logo colours as the base. These adverts are going to be used on our own site.
Regards
Thanks Hostmod for making that clear for designers.
Designers, we don't have images of the product we sell as we provide real estate services (not goods). If looking for inspiration for imagery, residential property is more appropriate than commercial property.
Thanks everyone.
Attention Designers!
PH is looking for static banner design which includes two individual advert frames.
Banner size : 450 wide x 225 high
I'm clarifying with our site technicians exactly what the frames should be.
We originally wanted two individual advert frames, 450 wide x 225 high, with no animation in the frames themselves. However, when trying to work within the Tandelvox fields, we couldn't elect the specific size we required and instead had to opt for a package deal.
I will upload a link to the real estate website template we will be using, the template has 'featured property' images in the centre of the homepage which we will be replacing with our two adverts. That is, we will not have the featured property on the home page at all.
http://skins.brovellanstudio.example/?theme=realestate2
Dear PH,
Is this animated gifs or flash?

```html
<!DOCTYPE html>
<html lang="en">
<head>
<meta charset="utf-8">
<title>Commission Savings Banner</title>
<link rel="stylesheet" href="https://fonts.googleapis.com/css2?family=Oswald:wght@600;700&family=Francois+One&display=swap">
<style>
  :root {
    --sky-top: #1d7fd6;
    --sky-bottom: #0b4f9f;
    --header-dark: #0c4c9c;
    --header-mid: #1565bd;
    --rim-light: #39a4ec;
    --headline: #ffffff;
    --bullet-text: #fff6c4;
    --icon-fill: #2f8ee0;
    --icon-edge: #bfe3ff;
    --shadow: rgba(0, 20, 60, 0.55);
  }
  html, body {
    margin: 0;
    padding: 0;
    width: 1200px;
    height: 600px;
    overflow: hidden;
    background: var(--sky-bottom);
  }
  .banner {
    display: block;
    width: 1200px;
    height: 600px;
  }
  .headline {
    font-family: "Oswald", sans-serif;
    font-weight: 700;
    fill: var(--headline);
  }
  .headline-shadow {
    font-family: "Oswald", sans-serif;
    font-weight: 700;
    fill: var(--shadow);
  }
  .benefit {
    font-family: "Francois One", sans-serif;
    fill: var(--bullet-text);
  }
  .benefit-shadow {
    font-family: "Francois One", sans-serif;
    fill: var(--shadow);
  }
</style>
</head>
<body>
<svg class="banner" viewBox="0 0 1200 600" xmlns="http://www.w3.org/2000/svg">
  <defs>
    <linearGradient id="panel-fill" x1="0" y1="0" x2="0" y2="1">
      <stop offset="0" stop-color="var(--sky-top)"/>
      <stop offset="1" stop-color="var(--sky-bottom)"/>
    </linearGradient>
    <linearGradient id="header-fill" x1="0" y1="0" x2="0" y2="1">
      <stop offset="0" stop-color="var(--header-mid)"/>
      <stop offset="1" stop-color="var(--header-dark)"/>
    </linearGradient>
    <linearGradient id="icon-fill" x1="0" y1="0" x2="1" y2="1">
      <stop offset="0" stop-color="#8fd0ff"/>
      <stop offset="1" stop-color="var(--icon-fill)"/>
    </linearGradient>
  </defs>

  <rect class="panel" x="0" y="0" width="1200" height="600" fill="url(#panel-fill)"/>

  <polygon class="header-rim" points="0,0 1200,0 1200,22 0,22" fill="var(--rim-light)"/>
  <polygon class="header-band" points="0,22 1150,22 1200,60 1200,168 0,168" fill="url(#header-fill)"/>
  <polygon class="header-fold" points="1150,0 1200,0 1200,60 1150,22" fill="#0a3f85"/>
  <rect class="header-edge" x="0" y="168" width="1200" height="4" fill="#2a8fe0"/>

  <g class="headline-group">
    <text class="headline-shadow" x="108" y="154" font-size="104" textLength="590" lengthAdjust="spacingAndGlyphs">SAVE THOUSANDS</text>
    <text class="headline" x="104" y="150" font-size="104" textLength="590" lengthAdjust="spacingAndGlyphs">SAVE THOUSANDS</text>
    <text class="headline-shadow" x="719" y="154" font-size="70" textLength="376" lengthAdjust="spacingAndGlyphs">IN COMMISSION</text>
    <text class="headline" x="716" y="150" font-size="70" textLength="376" lengthAdjust="spacingAndGlyphs">IN COMMISSION</text>
  </g>

  <g class="benefit-list">
    <g class="benefit-item">
      <rect x="110" y="262" width="40" height="40" fill="url(#icon-fill)" stroke="var(--icon-edge)" stroke-width="3"/>
      <path d="M118 282 l9 10 l18 -24" fill="none" stroke="#ffffff" stroke-width="5" stroke-linecap="round" stroke-linejoin="round"/>
      <text class="benefit-shadow" x="178" y="302" font-size="50" textLength="892" lengthAdjust="spacingAndGlyphs">PRIVATE PROPERTY SALES SOLUTIONS</text>
      <text class="benefit" x="175" y="299" font-size="50" textLength="892" lengthAdjust="spacingAndGlyphs">PRIVATE PROPERTY SALES SOLUTIONS</text>
    </g>
    <g class="benefit-item">
      <rect x="110" y="355" width="40" height="40" fill="url(#icon-fill)" stroke="var(--icon-edge)" stroke-width="3"/>
      <path d="M118 375 l9 10 l18 -24" fill="none" stroke="#ffffff" stroke-width="5" stroke-linecap="round" stroke-linejoin="round"/>
      <text class="benefit-shadow" x="178" y="395" font-size="50" textLength="918" lengthAdjust="spacingAndGlyphs">ASSISTED PROPERTY SALES EXPERTISE</text>
      <text class="benefit" x="175" y="392" font-size="50" textLength="918" lengthAdjust="spacingAndGlyphs">ASSISTED PROPERTY SALES EXPERTISE</text>
    </g>
    <g class="benefit-item">
      <rect x="110" y="448" width="40" height="40" fill="url(#icon-fill)" stroke="var(--icon-edge)" stroke-width="3"/>
      <path d="M118 468 l9 10 l18 -24" fill="none" stroke="#ffffff" stroke-width="5" stroke-linecap="round" stroke-linejoin="round"/>
      <text class="benefit-shadow" x="178" y="488" font-size="50" textLength="520" lengthAdjust="spacingAndGlyphs">NO HIDDEN CHARGES</text>
      <text class="benefit" x="175" y="485" font-size="50" textLength="520" lengthAdjust="spacingAndGlyphs">NO HIDDEN CHARGES</text>
    </g>
  </g>
</svg>
</body>
</html>
```